International Travel Technology R&D business needs a wordpress website

We are a start up team of initially 2 individuals but plan to grow our team quickly, we have deep experience in travel technology. Our goal is to provide next generation technology research and development on behalf of our clients who are leading players in the travel technology industry. Attached our logos.

Target Market(s)

Travel Technology companies

Industry/Entity Type

Travel Industry

Coding

Coded - Design and coding required

Font styles to use
Sans Serif

Requirements
Must have
• Make use of our logo and colour scheme in the attached. Has to have a sense of adventure/ stepping into the unknown but equally must convey a sense of professionalism , we are a safe pair of hands. Sample themes are in the attachment .
Nice to have
• We have identified a theme on layoutgrove which we feel would be inspirational. We hahe attached them to help in the design as inspiration.
Should not have
• images of airplanes , hotels etc, we want to project a future image.

```html
<!DOCTYPE html>
<html lang="en">
<head>
<meta charset="utf-8">
<title>Nexora Labs</title>
<link href="https://fonts.googleapis.com/css2?family=Open+Sans:wght@400;600;700&family=Questrial&display=swap" rel="stylesheet">
<style>
:root{
  --blue:#1ea3dd;
  --blue-dark:#1479b8;
  --green:#2fb96a;
  --ink:#333;
  --muted:#777;
  --light:#f0f0f0;
  --nav:#2f2f2f;
  --nav-dark:#222;
  --footer:#2b2b2b;
  --line:#dcdcdc;
}
*{box-sizing:border-box;margin:0;padding:0}
html,body{width:1200px;height:5187px;overflow:hidden}
body{font-family:"Open Sans",Arial,sans-serif;color:var(--ink);background:#fff;font-size:13px;line-height:1.55}
h1,h2,h3,.display{font-family:"Questrial","Century Gothic",sans-serif;font-weight:400}
.btn{display:inline-block;font-size:11px;font-weight:700;letter-spacing:.5px;color:#fff;padding:10px 22px;text-transform:uppercase}
.btn-green{background:var(--green)}
.btn-blue{background:var(--blue)}
.photo{display:block}

/* Header */
.site-header{height:180px;display:flex;align-items:center;padding:0 40px}
.brand{display:flex;align-items:center;gap:12px;width:370px}
.brand-dot{width:34px;height:34px;border-radius:50%;background:var(--blue);flex:none}
.brand-name{font-family:"Questrial",sans-serif;font-size:30px;color:var(--blue);letter-spacing:1px}
.contact-strip{display:flex;gap:44px;flex:1}
.contact-item{display:flex;align-items:center;gap:10px}
.contact-icon{width:32px;height:32px;border-radius:50%;border:2px solid var(--green);display:flex;align-items:center;justify-content:center;flex:none}
.contact-item small{display:block;font-size:11px;color:var(--muted)}
.contact-item strong{font-size:14px;font-weight:600}
.contact-item span.value{font-size:12px}
.social{display:flex;gap:8px}
.social i{width:28px;height:28px;border-radius:50%;background:var(--blue);display:block}

/* Nav */
.main-nav{height:48px;background:var(--nav);display:flex;justify-content:space-between;padding-left:40px}
.main-nav ul{list-style:none;display:flex}
.main-nav li{color:#fff;font-size:11px;font-weight:700;padding:0 16px;line-height:48px;text-transform:uppercase}
.main-nav li.active{border-bottom:3px solid var(--green)}
.appointment{background:var(--nav-dark);color:#fff;font-size:11px;font-weight:700;padding:0 30px;line-height:48px}

/* Hero */
.hero{height:509px;position:relative;background:linear-gradient(180deg,#3d5873 0%,#9a8a7a 45%,#d19a5c 62%,#2e3a48 100%)}
.hero-text{position:absolute;left:610px;top:195px;color:#fff}
.hero-text h1{font-size:34px}
.hero-text p{font-size:16px;margin:2px 0 16px}
.slide-arrow{position:absolute;top:235px;width:40px;height:44px;background:var(--blue);display:flex;align-items:center;justify-content:center}
.slide-arrow.prev{left:0}.slide-arrow.next{right:0}

/* Features */
.features{height:300px;display:flex;padding:85px 45px 0;gap:40px}
.feature{flex:1;display:flex;gap:14px}
.feature-num{font-family:"Questrial",sans-serif;font-size:46px;color:#c4c4c4;line-height:1}
.feature h3{font-family:"Open Sans",sans-serif;font-size:14px;font-weight:600;margin-bottom:4px}
.feature p{font-size:12px;color:var(--muted)}

/* Services */
.services{height:647px;margin-top:28px;position:relative;background:linear-gradient(90deg,#1a8fd2 0%,#2da3e2 30%,#1d4f86 55%,#0f2448 100%)}
.services-intro{position:absolute;left:60px;top:225px;width:250px;color:#fff}
.services-intro h2{font-size:42px;margin-bottom:10px}
.services-intro p{font-size:12px}
.services-panel{position:absolute;left:370px;top:85px;width:715px;height:480px;background:rgba(255,255,255,.92);display:grid;grid-template-columns:1fr 1fr;padding:40px 60px;gap:30px 60px}
.service{display:flex;gap:18px}
.service svg{flex:none}
.service h3{font-family:"Open Sans",sans-serif;font-size:14px;font-weight:600;color:var(--blue)}
.service p{font-size:12px;color:var(--muted)}

/* Stats */
.stats{height:225px;display:flex;justify-content:center;gap:110px;padding-top:50px;text-align:center}
.stat .display{font-size:62px;color:var(--green);line-height:1.1}
.stat p{font-size:15px}

/* FAQ */
.faq{height:550px;margin-top:10px;display:flex}
.faq-photo{width:590px;height:550px;margin-left:10px;background:linear-gradient(135deg,#cfd7de,#7b8793 60%,#3c4650)}
.faq-body{flex:1;padding:70px 55px 0 60px}
.faq-body h2{font-size:30px;text-align:center;margin-bottom:22px}
.faq-item{border:1px solid var(--line);margin-bottom:12px;font-size:14px;font-weight:600;padding:14px 18px;display:flex;justify-content:space-between;align-items:center}
.faq-item.open{background:var(--blue);color:#fff;border-color:var(--blue);margin-bottom:0}
.faq-answer{font-size:12px;color:var(--muted);padding:14px 18px 22px}

/* Projects */
.projects{height:788px;text-align:center;padding-top:85px}
.section-title{font-size:40px;margin-bottom:36px}
.project-grid{display:grid;grid-template-columns:repeat(3,360px);gap:10px 20px;justify-content:center;margin-bottom:48px}
.project-grid .photo{height:225px}
.t1{background:linear-gradient(160deg,#122a4a,#5a7fa8)}
.t2{background:linear-gradient(160deg,#e6e6e6,#333)}
.t3{background:linear-gradient(160deg,#3e4d6b,#d38d5a)}
.t4{background:linear-gradient(160deg,#dde6ee,#5b6a7a)}
.t5{background:linear-gradient(160deg,#9fb9cf,#1d3a5f)}
.t6{background:linear-gradient(160deg,#4c8fd0,#c7e2f5)}

/* Feedback */
.feedback{height:467px;border-top:1px solid #e5e5e5;text-align:center;padding-top:80px}
.feedback .section-title{margin-bottom:20px}
.feedback p.lead{width:1090px;margin:0 auto 44px;font-size:12px;color:var(--muted)}
.clients{display:flex;justify-content:center;gap:120px}
.client{display:flex;align-items:center;gap:16px;text-align:left}
.avatar{width:86px;height:86px;border-radius:50%;border:3px solid var(--green);background:linear-gradient(#e2d6cc,#a8988c)}
.client strong{display:block;font-size:14px;font-weight:600}
.client span{font-size:13px;color:var(--green);font-weight:600}

/* Call back */
.callback{height:536px;background:var(--light);position:relative}
.callback-form{position:absolute;left:75px;top:80px;width:640px}
.callback-form h2{font-size:40px;margin-bottom:20px}
.field-row{display:flex;gap:10px;margin-bottom:10px}
.field{flex:1;height:42px;background:#fff;border:1px solid var(--line);font-size:12px;font-weight:600;padding:12px 14px;display:flex;justify-content:space-between;align-items:center}
.field.message{height:100px;align-items:flex-start}
.callback-form .btn{margin-top:14px}
.callback-photo{position:absolute;right:20px;bottom:0;width:440px;height:480px;background:linear-gradient(180deg,#e6e8ea,#b4bfca 50%,#3d5c8a)}

/* News */
.news{height:570px;padding-top:85px;text-align:center}
.news .section-title{margin-bottom:30px}
.news-grid{display:grid;grid-template-columns:repeat(3,360px);gap:20px;justify-content:center;text-align:left}
.news-card .photo{height:230px;position:relative}
.n1{background:linear-gradient(150deg,#dbe4ea,#7d8f9c)}
.n2{background:linear-gradient(150deg,#2f7fc8,#0d2d55)}
.n3{background:linear-gradient(150deg,#3a4d6a,#8b9fb8)}
.date{position:absolute;right:10px;top:10px;background:#fff;text-align:center;width:56px;padding:4px 0}
.date b{display:block;font-size:24px;line-height:1.1}
.date span{font-size:11px;font-weight:700}
.news-card h4{font-size:12px;margin:20px 0 6px}
.news-card p{font-size:12px;color:var(--muted)}

/* Footer */
.site-footer{height:329px;background:var(--footer);color:#ccc;position:relative}
.footer-cols{display:flex;padding:55px 40px 0;gap:50px}
.footer-brand{width:200px;padding-top:55px;display:flex;align-items:center;gap:10px}
.footer-brand .brand-dot{width:26px;height:26px}
.footer-brand span{font-family:"Questrial",sans-serif;font-size:24px;color:#fff}
.footer-col h5{color:var(--green);font-size:11px;font-weight:700;text-transform:uppercase;margin-bottom:12px}
.footer-col ul{list-style:none;font-size:12px;line-height:1.55}
.footer-col .input{width:200px;height:30px;background:#fff;color:#555;font-size:11px;padding:6px 10px;margin-bottom:10px}
.footer-col .btn{padding:7px 14px;font-size:10px}
.footer-col p{font-size:12px;margin-bottom:10px;display:flex;gap:10px;align-items:flex-start}
.footer-call{position:absolute;right:30px;top:50px;width:275px;height:160px;background:var(--blue);border:4px solid #fff;border-radius:12px;color:#fff;text-align:center;padding-top:22px}
.footer-call small{font-size:14px;font-weight:700;display:block}
.footer-call strong{font-size:28px;font-weight:600;display:flex;align-items:center;justify-content:center;gap:8px;white-space:nowrap}
.footer-call .social{justify-content:center;margin-top:8px}
.footer-call .social i{background:#fff;width:24px;height:24px}
.copyright{position:absolute;bottom:0;left:0;right:0;height:36px;border-top:1px solid #444;text-align:center;font-size:10px;line-height:36px;color:#999}
</style>
</head>
<body>

<header class="site-header">
  <div class="brand"><span class="brand-dot"></span><span class="brand-name">NEXORA LABS</span></div>
  <div class="contact-strip">
    <div class="contact-item">
      <span class="contact-icon"><svg width="14" height="14" viewBox="0 0 24 24"><path d="M6 2l4 5-2 3a12 12 0 006 6l3-2 5 4-3 4C10 22 2 14 2 5z" fill="#2fb96a"/></svg></span>
      <div><small>Contact Us</small><strong>800-555-0142</strong></div>
    </div>
    <div class="contact-item">
      <span class="contact-icon"><svg width="14" height="14" viewBox="0 0 24 24"><path d="M12 2a7 7 0 00-7 7c0 5 7 13 7 13s7-8 7-13a7 7 0 00-7-7zm0 10a3 3 0 110-6 3 3 0 010 6z" fill="#2fb96a"/></svg></span>
      <div><small>Our Address</small><span class="value">45 Harbour Row, Lanmore, Ireland</span></div>
    </div>
    <div class="contact-item">
      <span class="contact-icon"><svg width="14" height="14" viewBox="0 0 24 24"><path d="M2 5h20v14H2z" fill="none" stroke="#2fb96a" stroke-width="2"/><path d="M2 5l10 8 10-8" fill="none" stroke="#2fb96a" stroke-width="2"/></svg></span>
      <div><small>Email Us</small><span class="value">info@nexoralabs.com</span></div>
    </div>
  </div>
  <div class="social"><i></i><i></i><i></i></div>
</header>

<nav class="main-nav">
  <ul>
    <li class="active">Home</li><li>About Us</li><li>Services</li><li>Projects</li><li>Portfolio</li><li>Latest News</li><li>Contact Us</li>
  </ul>
  <div class="appointment">GET AN APPOINTMENT</div>
</nav>

<section class="hero" role="img" aria-label="City skyline with a bridge and glass tower at sunset">
  <div class="hero-text">
    <h1>Welcome to Nexora Labs</h1>
    <p>Helping Your Travel Business Build and Grow</p>
    <span class="btn btn-green">Get in Touch</span>
  </div>
  <span class="slide-arrow prev"><svg width="12" height="16" viewBox="0 0 12 16"><path d="M10 2L3 8l7 6" fill="none" stroke="#fff" stroke-width="3"/></svg></span>
  <span class="slide-arrow next"><svg width="12" height="16" viewBox="0 0 12 16"><path d="M2 2l7 6-7 6" fill="none" stroke="#fff" stroke-width="3"/></svg></span>
</section>

<section class="features">
  <div class="feature"><span class="feature-num">01.</span><div><h3>Solutions</h3><p>Lorem ipsum dolor sit amet, consectetur adipiscing elit, sed diam nonummy euismod tincidunt ut laoreet dolore magna aliquam erat volutpat. Ut wisi enim ad minim veniam, quis nostrud exerci tation ullamcorper suscipit lobortis nisl ut aliquip commodo consequat.</p></div></div>
  <div class="feature"><span class="feature-num">02.</span><div><h3>Management</h3><p>Lorem ipsum dolor sit amet, consectetur adipiscing elit, sed diam nonummy euismod tincidunt ut laoreet dolore magna aliquam erat volutpat. Ut wisi enim ad minim veniam, quis nostrud exerci tation ullamcorper suscipit lobortis nisl ut aliquip commodo consequat.</p></div></div>
  <div class="feature"><span class="feature-num">03.</span><div><h3>Technology</h3><p>Lorem ipsum dolor sit amet, consectetur adipiscing elit, sed diam nonummy euismod tincidunt ut laoreet dolore magna aliquam erat volutpat. Ut wisi enim ad minim veniam, quis nostrud exerci tation ullamcorper suscipit lobortis nisl ut aliquip commodo consequat.</p></div></div>
</section>

<section class="services" role="img" aria-label="Blue city lights and network glow behind the services panel">
  <div class="services-intro">
    <h2>Our Services</h2>
    <p>Lorem ipsum dolor sit amet, consectetur adipiscing elit, sed diam nonummy nibh euismod tincidunt ut laoreet dolore magna aliquam erat volutpat. Ut wisi enim ad minim veniam, quis nostrud exerci tation ullamcorper suscipit lobortis nisl ut aliquip ex ea commodo.</p>
  </div>
  <div class="services-panel">
    <div class="service">
      <svg width="44" height="44" viewBox="0 0 44 44" fill="none" stroke="#444" stroke-width="2"><rect x="6" y="14" width="32" height="22" rx="2"/><path d="M16 14v-5h12v5M6 24h32"/></svg>
      <div><h3>Business Consulting</h3><p>Lorem ipsum dolor sit amet, consectetur adipiscing elit, sed diam nonummy nibh euismod tincidunt ut laoreet dolore magna aliquam erat volutpat. Ut wisi enim ad minim veniam, quis nostrud exerci tation ullamcorper suscipit lobortis nisl ut aliquip ex ea commodo consequat.</p></div>
    </div>
    <div class="service">
      <svg width="44" height="44" viewBox="0 0 44 44" fill="none" stroke="#444" stroke-width="2"><rect x="12" y="4" width="20" height="36" rx="3"/><path d="M19 35h6"/></svg>
      <div><h3>Technology Research</h3><p>Lorem ipsum dolor sit amet, consectetur adipiscing elit, sed diam nonummy nibh euismod tincidunt ut laoreet dolore magna aliquam erat volutpat. Ut wisi enim ad minim veniam, quis nostrud exerci tation ullamcorper suscipit lobortis nisl ut aliquip ex ea commodo consequat.</p></div>
    </div>
    <div class="service">
      <svg width="44" height="44" viewBox="0 0 44 44" fill="none" stroke="#444" stroke-width="2"><circle cx="22" cy="22" r="7"/><path d="M22 6v6M22 32v6M6 22h6M32 22h6M11 11l4 4M29 29l4 4M33 11l-4 4M15 29l-4 4"/></svg>
      <div><h3>Technology Development</h3><p>Lorem ipsum dolor sit amet, consectetur adipiscing elit, sed diam nonummy nibh euismod tincidunt ut laoreet dolore magna aliquam erat volutpat. Ut wisi enim ad minim veniam, quis nostrud exerci tation ullamcorper suscipit lobortis nisl ut aliquip ex ea commodo consequat.</p></div>
    </div>
    <div class="service">
      <svg width="44" height="44" viewBox="0 0 44 44" fill="none" stroke="#444" stroke-width="2"><rect x="12" y="12" width="20" height="20"/><path d="M17 12V6M22 12V6M27 12V6M17 38v-6M22 38v-6M27 38v-6M12 17H6M12 22H6M12 27H6M38 17h-6M38 22h-6M38 27h-6"/></svg>
      <div><h3>Implementation</h3><p>Lorem ipsum dolor sit amet, consectetur adipiscing elit, sed diam nonummy nibh euismod tincidunt ut laoreet dolore magna aliquam erat volutpat. Ut wisi enim ad minim veniam, quis nostrud exerci tation ullamcorper suscipit lobortis nisl ut aliquip ex ea commodo consequat.</p></div>
    </div>
  </div>
</section>

<section class="stats">
  <div class="stat"><div class="display">15+</div><p>Years of Business Operation</p></div>
  <div class="stat"><div class="display">780+</div><p>Clients Worldwide</p></div>
  <div class="stat"><div class="display">$2 Million +</div><p>Average profit earned<br>after using our service</p></div>
</section>

<section class="faq">
  <div class="faq-photo photo" role="img" aria-label="Business team talking in a glass office lobby"></div>
  <div class="faq-body">
    <h2>Frequently Asked Questions</h2>
    <div class="faq-item open">How can I initiate a project?<svg width="12" height="12" viewBox="0 0 12 12"><path d="M2 8l4-4 4 4" fill="none" stroke="#fff" stroke-width="2"/></svg></div>
    <p class="faq-answer">Lorem ipsum dolor sit amet, consectetur adipiscing elit, sed diam nonummy nibh euismod tincidunt ut laoreet dolore magna aliquam erat volutpat. Ut wisi enim ad minim veniam, quis nostrud exerci tation ullamcorper suscipit lobortis nisl ut aliquip ex ea commodo consequat.</p>
    <div class="faq-item">Where are your consultant based?<svg width="12" height="12" viewBox="0 0 12 12"><path d="M2 4l4 4 4-4" fill="none" stroke="#333" stroke-width="2"/></svg></div>
    <div class="faq-item">What is your service fee?<svg width="12" height="12" viewBox="0 0 12 12"><path d="M2 4l4 4 4-4" fill="none" stroke="#333" stroke-width="2"/></svg></div>
  </div>
</section>

<section class="projects">
  <h2 class="section-title">Our Recent Projects</h2>
  <div class="project-grid">
    <div class="photo t1" role="img" aria-label="City street with light trails at dusk"></div>
    <div class="photo t2" role="img" aria-label="Silhouettes of people at a conference table"></div>
    <div class="photo t3" role="img" aria-label="Aerial city view at sunset"></div>
    <div class="photo t4" role="img" aria-label="Team meeting around a table"></div>
    <div class="photo t5" role="img" aria-label="Business people reviewing documents"></div>
    <div class="photo t6" role="img" aria-label="Glass skyscrapers against blue sky"></div>
  </div>
  <span class="btn btn-blue">View All Projects</span>
</section>

<section class="feedback">
  <h2 class="section-title">Feedback From Our Clients</h2>
  <p class="lead">Lorem ipsum dolor sit amet, consectetur adipiscing elit, sed diam nonummy nibh euismod tincidunt ut laoreet dolore magna aliquam erat volutpat. Ut wisi enim ad minim veniam, quis nostrud exerci tation ullamcorper suscipit lobortis nisl ut aliquip ex ea commodo consequat. Duis autem vel eum iriure dolor in hendrerit in vulputate velit esse molestie consequat, vel illum dolore eu feugiat nulla facilisis at vero eros et accumsan et iusto odio dignissim.</p>
  <div class="clients">
    <div class="client"><span class="avatar" role="img" aria-label="Client portrait"></span><div><strong>Corinne Walsh</strong><span>CEO - Aerotrek Inc</span></div></div>
    <div class="client"><span class="avatar" role="img" aria-label="Client portrait"></span><div><strong>Clara Duval</strong><span>CEO - Globalroute Inc</span></div></div>
    <div class="client"><span class="avatar" role="img" aria-label="Client portrait"></span><div><strong>Brian Pratt</strong><span>CEO - Wayfarer Inc</span></div></div>
  </div>
</section>

<section class="callback">
  <div class="callback-form">
    <h2>Request a Call Back</h2>
    <div class="field-row"><div class="field">Name</div><div class="field">Email Address</div></div>
    <div class="field-row"><div class="field">Phone Number</div><div class="field">Topic To Discuss<svg width="10" height="10" viewBox="0 0 12 12"><path d="M2 4l4 4 4-4" fill="none" stroke="#333" stroke-width="2"/></svg></div></div>
    <div class="field-row"><div class="field message">Message</div></div>
    <span class="btn btn-blue">Send Request</span>
  </div>
  <div class="callback-photo photo" role="img" aria-label="Two smiling business professionals standing together"></div>
</section>

<section class="news">
  <h2 class="section-title">Latest News &amp; Updates</h2>
  <div class="news-grid">
    <article class="news-card">
      <div class="photo n1" role="img" aria-label="Colleagues working at a laptop"><div class="date"><b>24</b><span>JUL<br>2016</span></div></div>
      <h4>NEWS #1</h4>
      <p>Lorem ipsum dolor sit amet, consectetur adipiscing elit, sed diam nonummy nibh euismod tincidunt ut laoreet dolore magna aliquam erat volutpat.</p>
    </article>
    <article class="news-card">
      <div class="photo n2" role="img" aria-label="Water droplets on a blue glass surface"><div class="date"><b>22</b><span>JUL<br>2016</span></div></div>
      <h4>NEWS #2</h4>
      <p>Lorem ipsum dolor sit amet, consectetur adipiscing elit, sed diam nonummy nibh euismod tincidunt ut laoreet dolore magna aliquam erat volutpat.</p>
    </article>
    <article class="news-card">
      <div class="photo n3" role="img" aria-label="Business people in a meeting"><div class="date"><b>16</b><span>JUL<br>2016</span></div></div>
      <h4>NEWS #3</h4>
      <p>Lorem ipsum dolor sit amet, consectetur adipiscing elit, sed diam nonummy nibh euismod tincidunt ut laoreet dolore magna aliquam erat volutpat.</p>
    </article>
  </div>
</section>

<footer class="site-footer">
  <div class="footer-cols">
    <div class="footer-brand"><span class="brand-dot"></span><span>NEXORA LABS</span></div>
    <div class="footer-col"><h5>Quick Links</h5><ul><li>HOME</li><li>ABOUT US</li><li>SERVICES</li><li>PROJECTS</li><li>PORTFOLIO</li><li>LATEST NEWS</li><li>CONTACT US</li></ul></div>
    <div class="footer-col"><h5>Subscribe for Newsletter</h5><div class="input">Email Address</div><span class="btn btn-green">Subscribe</span></div>
    <div class="footer-col"><h5>Contact Us</h5>
      <p><svg width="12" height="14" viewBox="0 0 24 24"><path d="M12 2a7 7 0 00-7 7c0 5 7 13 7 13s7-8 7-13a7 7 0 00-7-7z" fill="#2fb96a"/></svg><span>45 Harbour Row<br>Lanmore, Ireland</span></p>
      <p><svg width="12" height="12" viewBox="0 0 24 24"><path d="M6 2l4 5-2 3a12 12 0 006 6l3-2 5 4-3 4C10 22 2 14 2 5z" fill="#2fb96a"/></svg><span>800-555-0142</span></p>
      <p><svg width="12" height="12" viewBox="0 0 24 24"><path d="M2 5h20v14H2z M2 5l10 8 10-8" fill="none" stroke="#2fb96a" stroke-width="2"/></svg><span>info@nexoralabs.com</span></p>
    </div>
  </div>
  <div class="footer-call">
    <small>CONTACT US TODAY</small>
    <strong><svg width="24" height="24" viewBox="0 0 24 24"><path d="M6 2l4 5-2 3a12 12 0 006 6l3-2 5 4-3 4C10 22 2 14 2 5z" fill="#fff"/></svg>800-555-0142</strong>
    <div class="social"><i></i><i></i><i></i></div>
  </div>
  <div class="copyright">COPYRIGHT © 2016 NEXORA LABS. ALL RIGHTS RESERVED.</div>
</footer>

</body>
</html>
```